Business Card - high end, modern health care

Hey designers!

We need a double sided business card for the boutique, cutting edge physical therapy rehabilitation centre in Sydney's Northern Beaches.

With the most qualified physios in the area The Harbourline Motion Clinic does what other physiotherapy practices do not, we take our time with our patients giving them longer appointments, better physios and therefor faster results!

We guarantee that the service people receive at THMC will be unparalleled.

Hence we need a business card to reflect our modern, boutique, high end service. The final design needs to reflect that we are in a class of our own yet with the feel of beachside retreat.

Below I have attached our logo in both blue on white and white on blue. The exact colour is;
and the font that we have used in our logo is Tex Gyre Aventador.

I like the idea of the blue as the main colour as it is more eye catching and our signage onto the main road will be in this blue and in the interest of consistency across marketing the blue needs to be a part of the design. However I would appreciate a few designs onto a wooden background as this is a visual theme within the fitout of the practice.

The design needs to be of standard size (91x55mm).

Target Market(s)

We target people who have an end outcome in mind and those who have had poor experiences with other providers and ensure that everyone gets the care that they deserve with a premium service that is tailored to the individuals circumstances. As a premium service, the target market is highly educated, business and tech savvy with the additional target market of elderly people who have self funded their retirement and see value in paying for the best ongoing rehabilitation to maintain independence.

Industry/Entity Type

Physical Therapy

Contact Information for Business Card

Name, designation( Titled Musculoskeletal Physiotherapist... there will also be those in the company that have multiple designations ie 5 or 6 words long), phone number, email, facebook, instagram, address

Font styles to use
Sans Serif

Colors

Designer to choose colors to be used in the design.

Requirements
Must have
• Front - The logo as large as possible, blue or wooden theme, and all of the important details.
• Back - A blank space/lines on which to write appointment times (no "Appointment, date, time" etc.)
Nice to have
• facebook url
• logos for facebook and instagram
• Mini logos for the phone and email?

```html
<!DOCTYPE html>
<html lang="en">
<head>
<meta charset="utf-8">
<title>The Harbourline Motion Clinic – Business Card</title>
<link href="https://fonts.googleapis.com/css2?family=Questrial&family=Roboto+Condensed:wght@400;700&display=swap" rel="stylesheet">
<style>
  :root{
    --brand-blue:#1f63b5;
    --brand-blue-deep:#18519a;
    --silver:#c7c9cc;
    --ink-light:#eef0f3;
    --paper:#f5f5f3;
    --backdrop:#1c1f24;
  }
  *{box-sizing:border-box;margin:0;padding:0}
  html,body{width:1200px;height:900px;overflow:hidden;background:var(--backdrop)}
  .stage{position:relative;width:1200px;height:900px}
  .card{position:absolute;left:280px;width:640px;height:387px;border-radius:24px;overflow:hidden}
  .card-front{top:40px;background:var(--brand-blue)}
  .card-back{top:473px;background:var(--paper)}

  /* front */
  .front-divider{position:absolute;inset:0}
  .front-brand{position:absolute;left:30px;top:30px;width:220px;text-align:center}
  .brand-dot{display:block;margin:0 auto 14px;width:130px;height:130px;border-radius:50%;background:var(--silver)}
  .brand-name{font-family:"Questrial",sans-serif;color:var(--silver);text-transform:uppercase;letter-spacing:2px;font-size:16px;line-height:1.3}
  .holder{position:absolute;right:30px;top:34px;text-align:right;color:var(--ink-light);font-family:"Roboto Condensed",sans-serif}
  .holder-name{font-size:34px;font-weight:700;letter-spacing:1px;text-transform:uppercase;line-height:1}
  .holder-title{font-size:17px;margin-top:6px}
  .treatment-art{position:absolute;right:30px;top:122px;width:150px;height:64px;border-radius:8px;background:linear-gradient(135deg,rgba(238,240,243,.35),rgba(238,240,243,.15))}
  .contacts{position:absolute;right:30px;top:200px;list-style:none;font-family:"Roboto Condensed",sans-serif;color:var(--ink-light);font-size:15px}
  .contacts li{display:flex;justify-content:flex-end;align-items:center;gap:10px;height:31px;white-space:nowrap}
  .contacts svg{width:18px;height:18px;flex:none}
  .social-box{width:16px;height:16px;border-radius:3px;background:var(--ink-light);flex:none;margin:0 1px}

  /* back */
  .back-rules{position:absolute;inset:0}
  .back-brand{position:absolute;left:300px;top:36px;width:260px;text-align:center}
  .back-brand .brand-dot{width:120px;height:120px;margin:0 auto 12px;background:var(--brand-blue)}
  .back-brand .brand-name{color:var(--brand-blue);font-size:15px;white-space:nowrap}
  .appointment{position:absolute;left:36px;top:250px;display:flex;align-items:flex-end;gap:16px}
  .appointment-arrow{width:22px;height:20px}
  .write-line{width:420px;border-bottom:1.5px dotted var(--brand-blue);margin-bottom:3px}
</style>
</head>
<body>
<main class="stage">

  <section class="card card-front">
    <svg class="front-divider" viewBox="0 0 640 387" aria-hidden="true">
      <path d="M370 0 Q360 330 0 360 L0 0 Z" fill="var(--brand-blue-deep)" opacity=".35"/>
      <path d="M370 0 Q360 330 0 360" fill="none" stroke="var(--silver)" stroke-width="7"/>
      <path d="M379 0 Q369 340 0 369" fill="none" stroke="#111" stroke-width="2"/>
    </svg>

    <div class="front-brand">
      <span class="brand-dot"></span>
      <p class="brand-name">The Harbourline<br>Motion Clinic</p>
    </div>

    <header class="holder">
      <h1 class="holder-name">Daniel Reyes</h1>
      <p class="holder-title">Musculoskeletal Physiotherapist</p>
    </header>

    <div class="treatment-art" role="img" aria-label="Pictograms of a therapist treating a patient on a table"></div>

    <ul class="contacts">
      <li>48 Shoreline Rd, Dee Why NSW
        <svg viewBox="0 0 24 24"><path d="M12 2a7 7 0 0 0-7 7c0 5 7 13 7 13s7-8 7-13a7 7 0 0 0-7-7zm0 9.5A2.5 2.5 0 1 1 12 6.5a2.5 2.5 0 0 1 0 5z" fill="var(--ink-light)"/></svg>
      </li>
      <li>+00 210 004 017
        <svg viewBox="0 0 24 24"><rect x="1" y="1" width="22" height="22" rx="4" fill="var(--ink-light)"/><path d="M8 5l2.5 3-1.5 2a9 9 0 0 0 5 5l2-1.5 3 2.5-1.5 2.5C11 18 6 13 5.5 6.5z" fill="var(--brand-blue)"/></svg>
      </li>
      <li>hello@harbourlinemotion.com
        <svg viewBox="0 0 24 24"><rect x="1" y="1" width="22" height="22" rx="4" fill="var(--ink-light)"/><rect x="5" y="7" width="14" height="10" fill="none" stroke="var(--brand-blue)" stroke-width="1.6"/><path d="M5 7l7 6 7-6" fill="none" stroke="var(--brand-blue)" stroke-width="1.6"/></svg>
      </li>
      <li>/harbourlinemotion <span class="social-box"></span></li>
      <li>@harbourlinemotion <span class="social-box"></span></li>
    </ul>
  </section>

  <section class="card card-back">
    <svg class="back-rules" viewBox="0 0 640 387" aria-hidden="true">
      <line x1="0" y1="206" x2="640" y2="206" stroke="var(--brand-blue)" stroke-width="2"/>
      <line x1="0" y1="215" x2="640" y2="215" stroke="var(--brand-blue)" stroke-width="2"/>
      <line x1="0" y1="312" x2="640" y2="312" stroke="var(--brand-blue)" stroke-width="2"/>
      <line x1="0" y1="321" x2="640" y2="321" stroke="var(--brand-blue)" stroke-width="2"/>
    </svg>

    <div class="back-brand">
      <span class="brand-dot"></span>
      <p class="brand-name">The Harbourline Motion Clinic</p>
    </div>

    <div class="appointment">
      <svg class="appointment-arrow" viewBox="0 0 22 20" aria-hidden="true"><path d="M0 0L22 10 0 20 5 10z" fill="var(--brand-blue)"/></svg>
      <span class="write-line"></span>
    </div>
  </section>

</main>
</body>
</html>
```